Harlow Creek Church Invite Card

We are a vibrant multigenerational church outside of Raleigh, NC and are wanting a 'church invite card' that we can encourage our members to carry with them so that they can invite their friends to church.

These cards should have a modern feel (see http://zentravio.com/neat-card-ideas/ for the feel we are going for), match the branding of our website (www.harlowcreek.org) and include the following information on the back:

Service Times: Sunday @ 9:15 AM and 10:45 AM (Main Focus)
Website: www.harlowcreek.org (Main Focus)
Social Media: (You can simply use the icons for these if desired)
www.plazebook.example/harlowcreekchurch
www.snapgrove.example/harlowcreekchurch
www.vidstream.example/harlowcreekyouth
Address: 4827 Marlow Avenue Ashmere, NC 27500 (Not a main focus)
Phone: (919) 555-0182 (Not a main focus)

The front should simply say 'We look forward to meeting you!'

Logos: Attached you will find the necessary logos for this project.

Fonts and Colors: Here are the specific colors (See HCC_Website_Color_Palette.pdf) and fonts that are used on our website.
Pacifico
Helvetica
Open Sans Regular

Target Market(s)

Friends of our congregation

Industry/Entity Type

Church

Contact Information for Business Card

We will likely print through Quillby Printworks. The details of what they need can be found here: http://www.quillbyprint.example/products/business-card

Font styles to use
Other font styles liked:
• Pacifico, Helvetica, Open Sans Regular, Bebas Nue

Colors
0592cd
34a7d8
85cae6
cee9f5
0455a3
3176b5
85acd3
cfdfed

Requirements
Must have
• Sleek, eye catching design
Nice to have
• Rounded Corners, Our social media sites (PB, Snapg and VidStream)

```html
<!DOCTYPE html>
<html lang="en">
<head>
<meta charset="utf-8">
<title>Harlow Creek Church Invite Card</title>
<link rel="stylesheet" href="https://fonts.googleapis.com/css2?family=Arimo:wght@400;500;700&family=Questrial&display=swap">
<style>
  :root {
    --page: #e4e4e4;
    --card-white: #ffffff;
    --ink: #111111;
    --brand-blue: #0a6ab8;
    --on-dark: #ffffff;
  }
  * { box-sizing: border-box; margin: 0; padding: 0; }
  html, body { width: 992px; height: 1200px; overflow: hidden; }
  body {
    background: var(--page);
    font-family: "Arimo", Helvetica, Arial, sans-serif;
    position: relative;
  }
  .card {
    position: absolute;
    left: 98px;
    width: 808px;
    height: 460px;
    border-radius: 24px;
    overflow: hidden;
  }
  .card-front { top: 104px; background: var(--card-white); }
  .card-back { top: 624px; background: var(--brand-blue); }
  .front-curve, .back-stripes { position: absolute; left: 0; top: 0; }
  .wordmark {
    position: absolute;
    font-family: "Questrial", "Arimo", sans-serif;
    font-weight: 400;
    letter-spacing: 1px;
    white-space: nowrap;
  }
  .card-front .wordmark {
    right: 40px; top: 84px;
    font-size: 42px;
    color: var(--ink);
  }
  .tagline {
    position: absolute;
    right: 40px; top: 220px;
    font-size: 19px;
    font-weight: 500;
    color: var(--ink);
  }
  .person { position: absolute; left: 36px; top: 268px; color: var(--on-dark); }
  .person-name { font-size: 27px; font-weight: 500; line-height: 1.2; }
  .person-role { font-size: 18px; margin-top: 2px; }
  .contact-list {
    position: absolute; left: 38px; top: 357px;
    list-style: none; color: var(--on-dark); font-size: 17.5px;
  }
  .contact-list li { display: flex; align-items: center; height: 26px; }
  .contact-list svg { width: 14px; height: 14px; margin-right: 16px; flex: none; }
  .social-list {
    position: absolute; right: 40px; top: 398px;
    display: flex; gap: 18px; list-style: none;
    color: var(--on-dark); font-size: 16px; font-weight: 700;
  }
  .card-back .wordmark {
    left: 0; right: 0; top: 152px; text-align: center;
    font-size: 46px; color: var(--on-dark);
  }
  .service-times {
    position: absolute; left: 0; right: 0; top: 316px;
    text-align: center; font-size: 25px; font-weight: 500; color: var(--on-dark);
  }
</style>
</head>
<body>
  <section class="card card-front">
    <svg class="front-curve" width="808" height="460" viewBox="0 0 808 460">
      <path d="M0,0 C110,220 400,342 808,346 L808,460 L0,460 Z" fill="var(--ink)"/>
    </svg>
    <div class="wordmark">Harlow Creek Church</div>
    <p class="tagline">'We look forward to meeting you!'</p>
    <div class="person">
      <div class="person-name">Marcus Tolliver</div>
      <div class="person-role">Managing Director</div>
    </div>
    <ul class="contact-list">
      <li><svg viewBox="0 0 14 14"><rect width="14" height="14" rx="2" fill="#fff"/><path d="M3 4h8v2H3zM4 7h6v4H4z" fill="#111"/></svg>(919) 555-0182</li>
      <li><svg viewBox="0 0 14 14"><rect width="14" height="14" rx="2" fill="#fff"/><circle cx="7" cy="7" r="4" fill="none" stroke="#111" stroke-width="1.4"/><path d="M3 7h8M7 3v8" stroke="#111" stroke-width="1"/></svg>www.harlowcreek.org</li>
      <li><svg viewBox="0 0 14 14"><rect width="14" height="14" rx="2" fill="#fff"/><path d="M7 2.5a3 3 0 0 1 3 3c0 2.2-3 6-3 6s-3-3.8-3-6a3 3 0 0 1 3-3z" fill="#111"/><circle cx="7" cy="5.5" r="1.1" fill="#fff"/></svg>4827 Marlow Avenue Ashmere, NC 27500</li>
    </ul>
    <ul class="social-list">
      <li>PB</li>
      <li>Snapg</li>
      <li>VidStream</li>
    </ul>
  </section>

  <section class="card card-back">
    <div class="wordmark">Harlow Creek Church</div>
    <p class="service-times">Service Times: Sunday @ 9:15 AM and 10:45 AM</p>
    <svg class="back-stripes" width="808" height="460" viewBox="0 0 808 460">
      <polygon points="0,402 378,402 384,418 0,418" fill="var(--ink)"/>
      <polygon points="384,402 808,402 808,418 390,418" fill="var(--on-dark)"/>
    </svg>
  </section>
</body>
</html>
```